Concert festival poster

Poster invitation for 40th party designed to look like a concert festival. Using the samples attached as a guide, looking for a colorful, creative and eye catching invite.
The event will be held over a weekend at a farm, with music food, friends and drinks.

Target Market(s)

Party guests, friends and family

Industry/Entity Type

Festival

Colors

Designer to choose colors to be used in the design.

Requirements
Must have
• Brellafest- Mark Telford's 40th festival
• Event date- 5-7th October 2018. Main event 6th October 2018 from 3pm-late
• Come anytime over the weekend- food, drinks and fun provided.
• Address is 412 Stony Creek Lane, Marulan NSW
• All welcome, including children
• Bring your own tent or let us know and we can arrange glamping tent set-up on site
• RSVP by 1 May 2018 to Kate at kate.anne.telford@mailbox-demo.com or Mark at mtelford@vantor-telford.com.au
• Will add extra information on event at later stage- see below for editable section.
Nice to have
• Editable section to add details, preferable at bottom of poster.

```html
<!DOCTYPE html>
<html lang="en">
<head>
<meta charset="utf-8">
<title>Brellafest – Mark Telford's 40th Festival</title>
<link rel="stylesheet" href="https://fonts.googleapis.com/css2?family=Fredoka:wght@500;600;700&family=Quicksand:wght@500;600&display=swap">
<style>
  :root {
    --page-bg: #e6e4df;
    --poster-bg: #2c3035;
    --sky-blue: #8fc6ea;
    --coral: #ec7f5c;
    --text-light: #e9ecef;
    --text-blue: #9ccbe8;
    --lemon: #f3e27a;
    --mint: #8fe0b8;
    --lilac: #c5a7ea;
    --pink: #f4a3c4;
  }
  * { margin: 0; padding: 0; box-sizing: border-box; }
  html, body {
    width: 1200px; height: 857px; overflow: hidden;
    background: var(--page-bg);
  }
  .poster {
    position: absolute; left: 330px; top: 19px;
    width: 540px; height: 819px;
    background: var(--poster-bg);
    color: var(--text-light);
    font-family: "Quicksand", sans-serif;
    box-shadow: 0 6px 24px rgba(0,0,0,.25);
    overflow: hidden;
  }
  .art-top {
    position: absolute; left: 0; top: 0; width: 540px; height: 128px;
    background:
      linear-gradient(180deg, rgba(44,48,53,0) 55%, var(--poster-bg) 100%),
      linear-gradient(90deg, rgba(243,226,122,.55), rgba(143,198,234,.5) 18%, rgba(236,127,92,.5) 34%, rgba(143,224,184,.5) 50%, rgba(244,163,196,.5) 66%, rgba(243,226,122,.5) 82%, rgba(143,224,184,.55));
  }
  .art-maracas {
    position: absolute; left: 10px; top: 580px; width: 68px; height: 100px;
    border-radius: 30px;
    background: linear-gradient(160deg, rgba(143,224,184,.5), rgba(236,127,92,.5));
  }
  .art-guitar {
    position: absolute; right: 10px; top: 572px; width: 62px; height: 128px;
    border-radius: 30px;
    background: linear-gradient(180deg, rgba(243,226,122,.5), rgba(143,198,234,.45));
  }
  .title { position: absolute; left: 28px; top: 146px; width: 484px; height: 220px; }
  .title text { font-family: "Fredoka", sans-serif; font-weight: 700; }
  .host { fill: var(--text-blue); font-size: 32px; }
  .age { font-size: 92px; }
  .festival { font-size: 98px; }
  .event-name { fill: var(--coral); font-size: 56px; }
  .dates {
    position: absolute; left: 28px; top: 368px;
    font-size: 14px; line-height: 19px; color: var(--text-blue);
  }
  .tagline {
    position: absolute; left: 0; top: 505px; width: 540px; text-align: center;
    font-family: "Fredoka", sans-serif; font-weight: 600;
    font-size: 23px; line-height: 30px; color: var(--coral);
    text-transform: uppercase; letter-spacing: .5px;
  }
  .details {
    position: absolute; left: 0; top: 585px; width: 540px; text-align: center;
    font-size: 15px; line-height: 19px;
  }
  .details p + p { margin-top: 15px; }
  .address {
    position: absolute; left: 0; top: 700px; width: 540px; text-align: center;
    font-size: 14px;
  }
  .divider {
    position: absolute; left: 28px; top: 730px; width: 484px;
    border-top: 1px dashed rgba(233,236,239,.45);
  }
  .rsvp {
    position: absolute; left: 0; top: 742px; width: 540px; text-align: center;
    font-size: 13px; line-height: 18px;
  }
</style>
</head>
<body>
  <main class="poster">
    <div class="art-top" role="img" aria-label="Colourful line drawings of musical instruments, notes and festival bunting along the top"></div>

    <svg class="title" viewBox="0 0 484 220" role="heading" aria-level="1" aria-label="Mark Telford's 40th Festival Brellafest">
      <defs>
        <linearGradient id="rainbow" x1="0" y1="0" x2="484" y2="0" gradientUnits="userSpaceOnUse">
          <stop offset="0" stop-color="#8fc6ea"/>
          <stop offset=".22" stop-color="#c5a7ea"/>
          <stop offset=".4" stop-color="#f4a3c4"/>
          <stop offset=".6" stop-color="#f3e27a"/>
          <stop offset=".8" stop-color="#8fe0b8"/>
          <stop offset="1" stop-color="#8fc6ea"/>
        </linearGradient>
      </defs>
      <text class="host" x="0" y="32" textLength="106" lengthAdjust="spacingAndGlyphs">MARK</text>
      <text class="host" x="0" y="64" textLength="188" lengthAdjust="spacingAndGlyphs">TELFORD'S</text>
      <text class="age" x="200" y="70" fill="url(#rainbow)" textLength="284" lengthAdjust="spacingAndGlyphs">40TH</text>
      <text class="festival" x="0" y="148" fill="url(#rainbow)" textLength="484" lengthAdjust="spacingAndGlyphs">FESTIVAL</text>
      <text class="event-name" x="0" y="206" textLength="484" lengthAdjust="spacingAndGlyphs">BRELLAFEST</text>
    </svg>

    <p class="dates">Event date- 5-7th October 2018.<br>Main event 6th October 2018 from 3pm-late</p>

    <p class="tagline">Come anytime over the weekend-<br>food, drinks and fun provided.</p>

    <div class="details">
      <p>All welcome, including children</p>
      <p>Bring your own tent or let us know and<br>we can arrange glamping tent set-up on site</p>
    </div>

    <div class="art-maracas" role="img" aria-label="Line drawing of a pair of maracas"></div>
    <div class="art-guitar" role="img" aria-label="Line drawing of a guitar"></div>

    <p class="address">Address is 412 Stony Creek Lane, Marulan NSW</p>
    <div class="divider"></div>
    <p class="rsvp">RSVP by 1 May 2018 to Kate at kate.anne.telford@mailbox-demo.com or<br>Mark at mtelford@vantor-telford.com.au</p>
  </main>
</body>
</html>
```